Creating business cards for our new private medical clinic in London

Hey everyone,

We are starting a new private medical clinic in central London. We already have our logo (please see the 2 different layouts of the logo attached.) Please note that we are not restricted to using only this font in the card though.

The cards will be printed by "Pekko." The cards have a textured surface and a coloured middle layer - please see this webpage for the exact product spec (https://www.pekkoprint.example/uk/products/velvet/business-cards.html). We're overall looking for a modern yet highly professional look. We'd like the cards to have Square edges and NOT rounded please.

We need a standard card that uses one or both of our logo's colours (blue and green), and another card for premium customers, that uses black with either gold/silver/bronze. On the black coloured cads, please could you add the word "Black Account" or the word "Black" under the logo text - wherever you think it looks best?

_________________

AMENDMENT TO BRIEF:

1) The first batch of our cards are to be promotional cards and need to have more information. Could please have one card that is more like an "information card" that has the following information: - (There's a lot there and we might need to slim this down once we see the cards.)

GP appointments £70
-Feeling unwell
-Referrals to private specialists
-Sexual health check up
-Contraception
-Second opinion

Launch Offer
First appointment £40 with this card until 30 September 2017

Book online

2) Could you see whether we could add a 'strap line' to the card, something like: “Stay in Optimal Health”

_____________

The files attached have 2 versions of our logo - one linear and with the words 'stacked'; we think that the stacked logo may work better for the business card but we'd love to see different versions.

On one side of the card could we please see a coloured background, with a design containing our logo? On the other side of the card, please could we have a different coloured or white background and the information below.

Address: THE HARROWFIELD CLINIC @ FitVanta, 19 Bramblecote Lane, London, EC2Z 4QJ
Open: Mon-Fri (early & late appointments)
Book Online: www.harrowfieldclinic.example
Email: bookings@harrowfieldclinic.example
Phone number: (We don't have this yet - but please leave a space for this to go into.)

Other possible design features:

Because our clinic is located in the financial district of London, anything that represents this (e.g. The City of London's skyline - i.e. financial district - could look nice (example buildings include: The Pinecone, The Teacup-Tower, The Wedgehouse, St Aldric Minster, Keep of Brennmoor, Gantry Crossing, The Spindle). We wondered whether a outline or drawing of these buildings in the background of the card could look nice. Please see the image link below to get an idea of the skyline we're looking for:

https://img.stockvale.example/z/skyline-hand-drawn-city-pastel-shades-heritage-buildings-futuristic-81920457.jpg

The following image links are examples of cards that we've seen online and like the overall feel of (of course our colours are different):

http://www.craftnook.example/diverse/2/goodcards/73014589122.jpg
http://cardheron.example/wp-content/uploads/2013/01/cool-business-cards-saffron.jpg
https://cardfolio.example/wp-content/uploads/20461-cool-business-card-mockup.jpg
http://www.plinthworks.example/wp-content/uploads/edd/2015/08/Modern-Tutor-Business-Card-Template-Preview.jpg
http://lorvelandkit.example/wp-content/uploads/2017/01/design-a-business-card-cool-business-card-designsqx83.jpg
http://makerspindle.example/resources/files/articles/harbor-print/copper-foil-business-cards.jpg

STATIONARY:
We will also need the following stationary designed by our chosen designer. We’d like stationary to use one or both the colours of our logo (ie Green and Blue). Please use these colours to add any additional design features to stationary - other similar palette colours can also be used. Our logo font is - abeatbyKai - and this could be used in other parts of the stationary, but please feel free to try other fonts too. We prefer sans serif fonts.

Overall - we are open to all ideas but we need a look and feel that looks modern and highly professional. For our letter, prescription and medical report templates we need these to be PDFs and word processing files that can merge relevant data and text into different sections.

The information required on various pieces of stationary are as follows:

Letterheads:
These need to have:
Clinic's: Logo / Address / Phone Number / Website / Email address / Recipients address.
The letter can have address data either at the top or as a footer. We're happy to see designs that use either to see which one looks best (same goes for other pieces of stationary too.)

Invoices:
Invoice number: (Unique code for document)
Invoice Date:
Clinic’s: Logo / Address / Phone Number / Website / Email address
Services: Service Code / Name of Service / Price
Total Price:
PAYLO, Cardwise and Northern Remit Logos
Patient details: Patient’s Name / Address

Prescription Pads:
Prescription number: (Unique code for document)
Clinic details: Clinic’s Logo / Address / Phone Number / Website / Email address
Patient details needed include: Patient’s Name / Date of birth / address
Blank space required to write the name of medication
Doctors Signature: and space for signature
MPB Number: and space for this to be entered

Templates for our medical reports:
These are reports we will be printed (on good quality paper) for patients after they have had a complete health check. They will include a text summary, and the results of any tests (with graphs) and images of scans. Please could we see how text/titles/headings/tables etc could be styled?
They will need the following details: -
Clinic details needed include: Clinic’s Logo / Address / Phone Number / Website / Email address
Date of Report:
Then the following sections need to be includes:
1) Free Text Space
2) Space for images and text
3) Space for blood test and text

___________________

Thanks so much everyone.

All the best,

Tev and Dane

Target Market(s)

City of London
Private Healthcare

Industry/Entity Type

Health Care

Contact Information for Business Card

Font styles to use
Sans Serif

Colors
33a6d7
25a0d3
add136
9bcb3c
cadf82
85acd3
3276b5
0255a3
85cae6

Requirements
Must have
• Please see project description for details.
Nice to have
• Perhaps a outline/drawing/illustration of the City of London skyline (i.e. the Pinecone and surrounding buildings)

```html
<!DOCTYPE html>
<html lang="en">
<head>
<meta charset="utf-8">
<title>The Harrowfield Clinic – Stationery Set</title>
<link rel="stylesheet" href="https://fonts.googleapis.com/css2?family=Lato:wght@300;400;700&display=swap">
<style>
  :root {
    --bg: #efefef;
    --paper: #ffffff;
    --blue: #55b8e0;
    --green: #add136;
    --green-light: #c4e03a;
    --green-deep: #a9cc2c;
    --green-tint: #e9f0d2;
    --ink: #1f1f1f;
    --ink-soft: #4a4a4a;
    --black-card: #141414;
  }
  * { box-sizing: border-box; margin: 0; padding: 0; }
  html, body { width: 1200px; height: 795px; overflow: hidden; }
  body {
    position: relative;
    background: var(--bg);
    font-family: "Lato", Arial, sans-serif;
    color: var(--ink);
  }
  .piece { position: absolute; overflow: hidden; }

  /* Brand lockup */
  .brand { position: absolute; display: flex; align-items: flex-start; }
  .brand__mark { flex: none; }
  .brand__text { display: flex; flex-direction: column; }
  .brand__name { font-weight: 300; line-height: 0.95; }
  .brand__tag { font-weight: 700; letter-spacing: 0.06em; text-transform: uppercase; }

  /* Letterhead */
  .letterhead { left: 292px; top: 99px; width: 295px; height: 416px; background: var(--paper); }
  .band { position: absolute; left: 0; top: 0; display: block; }
  .letterhead__address {
    position: absolute; left: 191px; top: 25px;
    font-size: 6.4px; line-height: 7.6px; font-weight: 700; color: var(--ink);
  }
  .letterhead__address span { font-weight: 400; display: block; }
  .letterhead__decor {
    position: absolute; right: 0; bottom: 0; width: 122px; height: 168px;
    background: var(--green-tint);
  }
  .contact-list {
    position: absolute; left: 17px; top: 373px; list-style: none;
    font-size: 5.4px; line-height: 8.7px; color: var(--ink-soft);
  }
  .contact-list li { display: flex; align-items: center; gap: 5px; }
  .contact-list i {
    display: inline-block; width: 4px; height: 4px; border-radius: 50%; background: var(--green);
  }

  /* Folder */
  .folder {
    left: 635px; top: 80px; width: 347px; height: 436px;
    background: radial-gradient(circle at 45% 40%, var(--green-light), var(--green-deep) 85%);
  }
  .folder__decor {
    position: absolute; left: 160px; top: 193px; width: 187px; height: 195px;
    background: rgba(120, 160, 20, 0.18);
  }
  .folder .brand { left: 104px; top: 196px; color: #fff; gap: 10px; }
  .folder .brand__mark { width: 14px; height: 14px; background: #fff; margin-top: 12px; }
  .folder .brand__name { font-size: 16px; }
  .folder .brand__tag { font-size: 5px; margin-top: 4px; }

  /* Business card – standard */
  .card-standard { left: 186px; top: 549px; width: 134px; height: 79px; background: var(--paper); }
  .card-standard__panel {
    position: absolute; left: 68px; top: 0; width: 66px; height: 79px; background: var(--green);
    color: #fff; padding: 20px 0 0 5px;
  }
  .card-standard__decor {
    position: absolute; right: 0; top: 0; width: 34px; height: 32px; background: rgba(120,160,20,0.25);
  }
  .card-standard__title { position: relative; font-size: 4px; letter-spacing: 0.04em; margin-bottom: 4px; }
  .card-standard__lines { position: relative; list-style: none; font-size: 2.6px; line-height: 4.8px; }
  .card-standard .brand { left: 5px; top: 34px; color: var(--blue); gap: 2px; align-items: center; }
  .card-standard .brand__mark { width: 6px; height: 6px; background: var(--green); }
  .card-standard .brand__name { font-size: 5px; }

  /* Business card – black */
  .card-black { left: 186px; top: 639px; width: 134px; height: 84px; background: var(--black-card); }
  .card-black__decor {
    position: absolute; left: 0; top: 0; width: 50px; height: 30px; background: rgba(255,255,255,0.06);
  }
  .card-black .brand { left: 38px; top: 34px; color: var(--blue); gap: 4px; }
  .card-black .brand__mark { width: 8px; height: 8px; background: var(--green); margin-top: 4px; }
  .card-black .brand__name { font-size: 6.5px; }
  .card-black .brand__tag { font-size: 2px; color: #bbb; margin-top: 2px; }

  /* Envelope – front */
  .envelope-front { left: 353px; top: 562px; width: 328px; height: 157px; background: var(--paper); }
  .envelope-front .brand { left: 16px; top: 38px; color: var(--blue); gap: 6px; }
  .envelope-front .brand__mark { width: 10px; height: 10px; background: var(--green); margin-top: 8px; }
  .envelope-front .brand__name { font-size: 9.5px; }
  .envelope-front .brand__tag { font-size: 2.6px; color: var(--ink-soft); margin-top: 3px; }
  .envelope-front__decor {
    position: absolute; left: 250px; top: 72px; width: 78px; height: 85px;
    background: rgba(0,0,0,0.035);
  }
  .envelope-front__address {
    position: absolute; left: 17px; top: 129px;
    font-size: 4.8px; line-height: 5.8px; font-weight: 700;
  }
  .envelope-front__address span { display: block; font-weight: 400; }

  /* Envelope – back */
  .envelope-back { left: 714px; top: 561px; width: 328px; height: 158px; background: var(--green-light); }
  .envelope-back__flap {
    position: absolute; left: 0; top: 0; width: 328px; height: 55px;
    background: var(--blue); border-radius: 0 0 10px 10px;
  }
  .envelope-back__decor {
    position: absolute; left: 0; top: 93px; width: 51px; height: 65px; background: rgba(120,160,20,0.2);
  }
  .envelope-back .brand { left: 128px; top: 13px; color: #fff; gap: 6px; }
  .envelope-back .brand__mark { width: 10px; height: 10px; background: #fff; margin-top: 6px; }
  .envelope-back .brand__name { font-size: 9.5px; }
  .envelope-back .brand__tag { font-size: 2.6px; margin-top: 3px; }
</style>
</head>
<body>

  <!-- Letterhead -->
  <section class="piece letterhead" aria-label="Letterhead">
    <svg class="band" width="295" height="11" viewBox="0 0 295 11" aria-hidden="true">
      <polygon points="0,0 68,0 62,11 0,11" fill="var(--blue)"/>
      <polygon points="76,0 152,0 146,11 70,11" fill="var(--green)"/>
      <polygon points="156,0 232,0 226,11 150,11" fill="var(--blue)"/>
      <polygon points="236,0 295,0 295,11 230,11" fill="var(--green)"/>
    </svg>
    <p class="letterhead__address">THE HARROWFIELD CLINIC
      <span>FitVanta, 19 Bramblecote Lane</span>
      <span>London, EC2Z 4QJ</span>
    </p>
    <div class="letterhead__decor" aria-hidden="true"></div>
    <ul class="contact-list">
      <li><i></i>123 4567 8900</li>
      <li><i></i>123 4567 8900</li>
      <li><i></i>bookings@harrowfieldclinic.example</li>
      <li><i></i>www.harrowfieldclinic.example</li>
    </ul>
  </section>

  <!-- Presentation folder -->
  <section class="piece folder" aria-label="Presentation folder">
    <div class="folder__decor" aria-hidden="true"></div>
    <div class="brand">
      <span class="brand__mark"></span>
      <div class="brand__text">
        <span class="brand__name">The<br>Harrowfield<br>Clinic</span>
        <span class="brand__tag">Private General Practice</span>
      </div>
    </div>
  </section>

  <!-- Standard business card -->
  <section class="piece card-standard" aria-label="Business card">
    <div class="brand">
      <span class="brand__mark"></span>
      <span class="brand__name">The Harrowfield Clinic</span>
    </div>
    <div class="card-standard__panel">
      <div class="card-standard__decor" aria-hidden="true"></div>
      <p class="card-standard__title">THE HARROWFIELD CLINIC</p>
      <ul class="card-standard__lines">
        <li>19 Bramblecote Lane, London</li>
        <li>123 4567 8900</li>
        <li>bookings@harrowfieldclinic.example</li>
        <li>www.harrowfieldclinic.example</li>
      </ul>
    </div>
  </section>

  <!-- Black business card -->
  <section class="piece card-black" aria-label="Premium business card">
    <div class="card-black__decor" aria-hidden="true"></div>
    <div class="brand">
      <span class="brand__mark"></span>
      <div class="brand__text">
        <span class="brand__name">The<br>Harrowfield<br>Clinic</span>
        <span class="brand__tag">Private General Practice</span>
      </div>
    </div>
  </section>

  <!-- Envelope front -->
  <section class="piece envelope-front" aria-label="Envelope front">
    <svg class="band" width="328" height="12" viewBox="0 0 328 12" aria-hidden="true">
      <polygon points="0,0 72,0 66,12 0,12" fill="var(--blue)"/>
      <polygon points="80,0 166,0 160,12 74,12" fill="var(--green)"/>
      <polygon points="172,0 252,0 246,12 166,12" fill="var(--blue)"/>
      <polygon points="260,0 328,0 328,12 254,12" fill="var(--green)"/>
    </svg>
    <div class="brand">
      <span class="brand__mark"></span>
      <div class="brand__text">
        <span class="brand__name">The<br>Harrowfield<br>Clinic</span>
        <span class="brand__tag">Private General Practice</span>
      </div>
    </div>
    <div class="envelope-front__decor" role="img" aria-label="Faint interlaced ornament"></div>
    <p class="envelope-front__address">THE HARROWFIELD CLINIC
      <span>FitVanta, 19 Bramblecote Lane</span>
      <span>London, EC2Z 4QJ</span>
    </p>
  </section>

  <!-- Envelope back -->
  <section class="piece envelope-back" aria-label="Envelope back">
    <div class="envelope-back__flap"></div>
    <div class="envelope-back__decor" aria-hidden="true"></div>
    <div class="brand">
      <span class="brand__mark"></span>
      <div class="brand__text">
        <span class="brand__name">The<br>Harrowfield<br>Clinic</span>
        <span class="brand__tag">Private General Practice</span>
      </div>
    </div>
  </section>

</body>
</html>
```